The Brightwater Compass Business Card

We need an attractive business card with the logo that we bought from ArtVantly last year.
Our mission is to contribute to change the way today's leaders manage business companies bringing value to the workplace and helping them to build a new model of creating wealth.
Our logo is clear about our values : we seek Positive Change through People and are convinced that the pursuit of individual well-being and the chase of economic results can converge with the right management.
Management Consulting
Corinne Fabrelle
+34 612 98 70 31
corinne.fabrelle@thebrightwatercompass-mail.net
www.thebrightwatercompass-mail.net

```html
<!DOCTYPE html>
<html lang="en">
<head>
<meta charset="utf-8">
<title>The Brightwater Compass – Business Card</title>
<link href="https://fonts.googleapis.com/css2?family=Cinzel:wght@400;500&family=Open+Sans:wght@400;600&display=swap" rel="stylesheet">
<style>
  :root {
    --page-bg: #c6c6c6;
    --teal: #0fa388;
    --teal-deep: #0b8f78;
    --teal-ink: #1a6f64;
    --mint: #d3f0ec;
    --mint-soft: #c2e8e2;
    --white: #ffffff;
    --edge: #e8e8e8;
  }
  * { box-sizing: border-box; margin: 0; padding: 0; }
  html, body {
    width: 1200px; height: 1200px; overflow: hidden;
    background: var(--page-bg);
  }
  .sheet {
    width: 1200px; height: 1200px;
    display: flex; flex-direction: column; align-items: center; justify-content: center;
    gap: 60px;
  }
  .card {
    position: relative;
    width: 840px; height: 480px;
    border-radius: 26px;
    overflow: hidden;
    box-shadow: 0 0 0 3px var(--edge), 0 14px 30px rgba(0,0,0,0.18);
  }

  /* Front */
  .card--front { background: linear-gradient(160deg, var(--teal) 0%, var(--teal-deep) 100%); }
  .front__map {
    position: absolute; inset: 0;
    background: radial-gradient(ellipse at 45% 50%, rgba(255,255,255,0.12) 0%, rgba(255,255,255,0.04) 60%, rgba(255,255,255,0) 100%);
  }
  .brand {
    position: absolute; inset: 0;
    display: flex; flex-direction: column; align-items: center; justify-content: center;
    gap: 26px;
  }
  .brand__mark {
    width: 78px; height: 78px; border-radius: 50%;
    background: var(--white);
  }
  .brand__name {
    font-family: "Cinzel", serif;
    font-weight: 400;
    font-size: 40px;
    letter-spacing: 3px;
    text-transform: uppercase;
    color: var(--white);
  }

  /* Back */
  .card--back { background: var(--mint); display: flex; }
  .contact-strip {
    width: 440px; height: 100%;
    background: var(--teal);
    display: flex; flex-direction: column; justify-content: center;
    gap: 34px;
    padding: 0 30px;
  }
  .contact-row {
    display: flex; align-items: center; gap: 14px;
    font-family: "Open Sans", sans-serif;
    font-size: 13.5px;
    color: var(--white);
    white-space: nowrap;
  }
  .contact-row__icon {
    flex: none;
    width: 34px; height: 34px; border-radius: 50%;
    background: var(--white);
    display: flex; align-items: center; justify-content: center;
  }
  .contact-row__icon svg { width: 18px; height: 18px; }
  .back__brand {
    flex: 1;
    position: relative;
    display: flex; flex-direction: column; align-items: center; justify-content: center;
    gap: 20px;
  }
  .back__map {
    position: absolute; inset: 0;
    background: radial-gradient(ellipse at 50% 50%, var(--mint-soft) 0%, var(--mint) 70%);
  }
  .back__brand .brand__mark { position: relative; width: 56px; height: 56px; background: var(--teal-ink); }
  .back__brand .brand__name {
    position: relative;
    font-size: 24px; letter-spacing: 2px;
    color: var(--teal-ink);
    text-align: center;
    line-height: 1.4;
  }
</style>
</head>
<body>
<main class="sheet">

  <section class="card card--front" aria-label="Business card front">
    <div class="front__map" role="img" aria-label="Faint world map across the card background"></div>
    <div class="brand">
      <span class="brand__mark"></span>
      <p class="brand__name">The Brightwater Compass</p>
    </div>
  </section>

  <section class="card card--back" aria-label="Business card back">
    <div class="contact-strip">
      <div class="contact-row">
        <span class="contact-row__icon">
          <svg viewBox="0 0 24 24"><path fill="#0fa388" d="M6.6 10.8a15.1 15.1 0 0 0 6.6 6.6l2.2-2.2a1 1 0 0 1 1-.25 11.4 11.4 0 0 0 3.6.57 1 1 0 0 1 1 1V20a1 1 0 0 1-1 1A17 17 0 0 1 3 4a1 1 0 0 1 1-1h3.5a1 1 0 0 1 1 1c0 1.25.2 2.45.57 3.57a1 1 0 0 1-.25 1z"/></svg>
        </span>
        <span>+34 612 98 70 31</span>
      </div>
      <div class="contact-row">
        <span class="contact-row__icon">
          <svg viewBox="0 0 24 24"><rect x="3" y="6" width="18" height="12" rx="1.5" fill="#0fa388"/><path d="M3.5 7l8.5 6 8.5-6" fill="none" stroke="#fff" stroke-width="1.6"/></svg>
        </span>
        <span>corinne.fabrelle@thebrightwatercompass-mail.net</span>
      </div>
      <div class="contact-row">
        <span class="contact-row__icon">
          <svg viewBox="0 0 24 24"><circle cx="12" cy="12" r="8.5" fill="none" stroke="#0fa388" stroke-width="1.8"/><path d="M3.5 12h17M12 3.5c-3 3-3 14 0 17M12 3.5c3 3 3 14 0 17" fill="none" stroke="#0fa388" stroke-width="1.5"/></svg>
        </span>
        <span>www.thebrightwatercompass-mail.net</span>
      </div>
    </div>
    <div class="back__brand">
      <div class="back__map" role="img" aria-label="Soft world map behind the brand name"></div>
      <span class="brand__mark"></span>
      <p class="brand__name">The Brightwater<br>Compass</p>
    </div>
  </section>

</main>
</body>
</html>
```